Tallwood Gatherings brochure

We need a brochure designed that is modern, high impact and grabs potential customers attention. I have provided a draft mock brochure as an example and to provide the desired information. The lay out and design can be changed.

The front to include image (examples provided. I may provide other images if I can source) Logo, Joining the Community, and perhaps a Community Access and Lifestyle Support Service, Specialising in Lifestyle and Recreation

Refer to website for information on the service www.tallwoodgatherings.com.au

Use colours of logo for design

Target Market(s)

KTRV participants (People with a disability and their family)

Colors

Designer to choose colors to be used in the design.

Requirements
Must have
• Image/s of people, logo, text in mock up design. Example images provided. Will source more images and upload.
Nice to have
• More than one image

```html
<!DOCTYPE html>
<html lang="en">
<head>
<meta charset="utf-8">
<title>Tallwood Gatherings – Brochure Inside Spread</title>
<link rel="stylesheet" href="https://fonts.googleapis.com/css2?family=Montserrat:wght@400;500;600;700;800&display=swap">
<style>
  :root {
    --green: #5aaa3c;
    --green-dark: #3f8f2a;
    --green-text: #4a9e31;
    --yellow: #f3cf6a;
    --yellow-soft: #fbeab4;
    --paper: #ffffff;
    --ink: #4a4a4a;
    --ink-strong: #2f2f2f;
    --photo-tint: #dfe8d6;
    --backdrop: #dcdcdc;
  }
  * { box-sizing: border-box; margin: 0; padding: 0; }
  html, body {
    width: 1200px; height: 960px; overflow: hidden;
    background: var(--backdrop);
    font-family: "Montserrat", Arial, sans-serif;
    color: var(--ink);
  }
  .spread {
    position: absolute; left: 60px; top: 62px;
    width: 1080px; height: 836px;
    display: flex;
    background: var(--paper);
    box-shadow: 0 6px 24px rgba(0,0,0,.18);
  }
  .panel {
    position: relative; width: 360px; height: 100%;
    overflow: hidden;
    background: linear-gradient(180deg, var(--yellow) 0, var(--yellow-soft) 60px, var(--paper) 170px);
  }
  .panel + .panel { border-left: 1px solid #ececec; }
  .panel-photo {
    position: absolute; left: 0; right: 0; top: 120px; bottom: 120px;
    background: radial-gradient(ellipse at 50% 45%, var(--photo-tint) 0%, rgba(223,232,214,.55) 45%, rgba(255,255,255,0) 78%);
    opacity: .9;
  }
  .panel-content { position: relative; padding-top: 34px; }
  .tab {
    display: block; background: var(--green);
    color: #fff; font-weight: 800; text-transform: uppercase;
    font-size: 22px; letter-spacing: 1px; line-height: 1.1;
    padding: 12px 22px;
    box-shadow: 0 2px 4px rgba(0,0,0,.15);
  }
  .tab--left { margin-right: 40px; border-radius: 0 18px 18px 0; padding-left: 40px; }
  .tab--right { margin-left: 40px; border-radius: 18px 0 0 18px; }
  .tab--center { margin: 0 30px; border-radius: 18px; text-align: center; }
  .body-text { font-size: 11.5px; line-height: 1.55; padding: 12px 32px 20px; }
  .lead {
    color: var(--green-text); font-weight: 700; font-size: 16px;
    padding: 14px 32px 4px; line-height: 1.2;
  }
  .bullets { list-style: none; font-size: 11.5px; line-height: 1.5; padding: 0 28px 18px 32px; }
  .bullets li { padding-left: 10px; position: relative; }
  .bullets li::before { content: "•"; position: absolute; left: 0; }
  .value-title {
    color: var(--green-text); font-weight: 800; font-size: 17px;
    text-transform: uppercase; letter-spacing: 1px; text-align: center;
    margin-top: 26px;
  }
  .value-text { font-size: 11.5px; line-height: 1.6; text-align: center; padding: 10px 36px 0; font-style: italic; }
  .brand {
    display: flex; align-items: center; justify-content: center; gap: 12px;
    margin-top: 56px;
  }
  .brand-dot { width: 46px; height: 46px; border-radius: 50%; background: var(--green); }
  .brand-name { color: var(--green-text); font-weight: 600; font-size: 22px; line-height: 1.15; }
  .note { font-weight: 700; color: var(--ink-strong); font-size: 11.5px; line-height: 1.5; padding: 4px 32px 22px; }
  .apply-text { font-weight: 700; color: var(--ink-strong); font-size: 12px; line-height: 1.5; padding: 14px 32px; }
</style>
</head>
<body>
  <main class="spread">
    <section class="panel panel--about">
      <div class="panel-photo" role="img" aria-label="Faded photograph of a support worker sharing an activity with a participant"></div>
      <div class="panel-content">
        <h2 class="tab tab--left">Who We Are</h2>
        <p class="body-text">A family driven lifestyle, recreation and leisure support service operated by a Management Committee consisting of parents and interested community members.</p>
        <h2 class="tab tab--left">Who We Assist</h2>
        <p class="lead">People with a disability who:</p>
        <ul class="bullets">
          <li>are over the age of 16 years;</li>
          <li>reside in the Cairns region, from Gordonvale to Palm Cove;</li>
          <li>meet the Northern Region Disability Services eligibility criteria;</li>
          <li>are registered as Kindred Regional Voucher Scheme (KTRV) participants after rollout in Cairns in July 2018; and/or</li>
          <li>have their own financial resources.</li>
        </ul>
        <h2 class="tab tab--left">Role of Family/<br>Advocate</h2>
        <p class="body-text">Families are our greatest resource and we actively seek their input to help the person with a disability maximize choice and control over their own lives.</p>
      </div>
    </section>

    <section class="panel panel--philosophy">
      <div class="panel-photo" role="img" aria-label="Faded photograph of smiling participants enjoying a community outing"></div>
      <div class="panel-content">
        <h2 class="tab tab--center">Our Philosophy</h2>
        <h3 class="value-title">Choice</h3>
        <p class="value-text">Choice is a key element in lifestyle, recreation and leisure pursuits, and we tailor support to meet people’s personal plans and goals.</p>
        <h3 class="value-title">Inclusion</h3>
        <p class="value-text">We believe that supporting people individually is the best way to enable them to attain a valued role in their community.</p>
        <h3 class="value-title">Opportunity</h3>
        <p class="value-text">All people have the right to be part of their community and to experience life’s opportunities.</p>
        <div class="brand">
          <span class="brand-dot"></span>
          <span class="brand-name">Tallwood<br>Gatherings</span>
        </div>
      </div>
    </section>

    <section class="panel panel--contact">
      <div class="panel-photo" role="img" aria-label="Faded photograph of a participant and carer together outdoors"></div>
      <div class="panel-content">
        <h2 class="tab tab--right">How to Find Us</h2>
        <p class="lead">We assist people to:</p>
        <ul class="bullets">
          <li>plan what support they need;</li>
          <li>choose suitable support people;</li>
          <li>accomplish daily living activities;</li>
          <li>participate in social and community activities;</li>
          <li>enhance and maintain independence, self confidence and self esteem;</li>
          <li>build capacity and improve or maintain skills;</li>
          <li>keep a job by supporting people in the work-place;</li>
          <li>improve lifelong learning;</li>
          <li>maintain health and wellbeing; and</li>
          <li>achieve their goals and desired outcomes.</li>
        </ul>
        <p class="lead">We employ support people to assist individuals:</p>
        <ul class="bullets">
          <li>on a one to one ratio;</li>
          <li>in their home and in generic community settings;</li>
          <li>to implement their personal plan;</li>
          <li>to access community services; and</li>
          <li>to meet their changing needs.</li>
        </ul>
        <p class="note">We can provide 24 hour support but all support is in non-segregated settings.</p>
        <h2 class="tab tab--right">How to Apply</h2>
        <p class="apply-text">Please contact our office to discuss how Tallwood Gatherings can support you.</p>
      </div>
    </section>
  </main>
</body>
</html>
```